Business Card Design

I would like a new business card design for an accounting firm that specializes in resolving clients tax problems. I want the card to give the impression that we are not your typical stodgy accounting firm, but at the same time we will get the job done.
Industry/Entity Type
Business
Contact Information for Business Card
Dorian T Welsby
Certified Public Accountant
38-27 52nd Street
Sunnyside, NY 11287
Tel: (718) 555-0142
Fax: (888) 555-0199
e-mail: dtwthecpa@ledgerpost.com
website: harborfilingreliefexperts.com

```html
<!DOCTYPE html>
<html lang="en">
<head>
<meta charset="utf-8">
<title>Dorian T Welsby – Business Card</title>
<link rel="stylesheet" href="https://fonts.googleapis.com/css2?family=Josefin+Sans:wght@400;600&display=swap">
<style>
  :root {
    --page-bg: #2a2a2a;
    --card-bg: #ffffff;
    --ink: #1c1c1c;
    --rule: #2b2b2b;
  }
  * { margin: 0; padding: 0; box-sizing: border-box; }
  html, body {
    width: 1200px;
    height: 800px;
    overflow: hidden;
    background: var(--page-bg);
  }
  .canvas {
    position: relative;
    width: 1200px;
    height: 800px;
    display: flex;
    align-items: center;
    justify-content: center;
  }
  .business-card {
    width: 700px;
    height: 400px;
    background: var(--card-bg);
    box-shadow: 0 10px 30px rgba(0, 0, 0, 0.45);
  }
  .business-card svg { display: block; }
  .card-text {
    font-family: "Josefin Sans", "Futura", sans-serif;
    fill: var(--ink);
  }
  .holder-name {
    font-size: 34px;
    font-weight: 600;
    letter-spacing: 1.5px;
  }
  .detail {
    font-size: 16px;
    font-weight: 400;
    letter-spacing: 0.4px;
  }
  .frame-line {
    fill: none;
    stroke: var(--rule);
    stroke-width: 1.6;
    stroke-linejoin: round;
  }
  .frame-fill {
    fill: var(--card-bg);
    stroke: var(--rule);
    stroke-width: 1.8;
    stroke-linejoin: round;
  }
</style>
</head>
<body>
  <main class="canvas">
    <article class="business-card">
      <svg width="700" height="400" viewBox="0 0 700 400" aria-label="Business card for Dorian T Welsby, Certified Public Accountant">
        <!-- diagonal accent running behind the frame -->
        <line class="frame-line" x1="518" y1="0" x2="203" y2="400"/>

        <!-- hand-drawn information frame -->
        <polygon class="frame-fill" points="120,62 582,57 584,343 118,346"/>
        <path class="frame-line" d="M119,131 L583,127"/>
        <path class="frame-line" d="M119,203 L583,200"/>
        <path class="frame-line" d="M118,273 L584,270"/>
        <path class="frame-line" d="M352,130 L353,202"/>

        <!-- name -->
        <text class="card-text holder-name" x="351" y="110" text-anchor="middle">DORIAN T WELSBY</text>

        <!-- title -->
        <text class="card-text detail" x="140" y="162">CERTIFIED</text>
        <text class="card-text detail" x="140" y="183">PUBLIC ACCOUNTANT</text>

        <!-- phone -->
        <text class="card-text detail" x="372" y="160">Tel: (718) 555-0142</text>
        <text class="card-text detail" x="372" y="181">Fax: (888) 555-0199</text>

        <!-- online -->
        <text class="card-text detail" x="351" y="232" text-anchor="middle">e-mail: dtwthecpa@ledgerpost.com</text>
        <text class="card-text detail" x="351" y="254" text-anchor="middle">website: harborfilingreliefexperts.com</text>

        <!-- address -->
        <text class="card-text detail" x="351" y="302" text-anchor="middle">38-27 52nd Street</text>
        <text class="card-text detail" x="351" y="324" text-anchor="middle">Sunnyside, NY 11287</text>
      </svg>
    </article>
  </main>
</body>
</html>
```